依頼詳細
◇サイトマップ
①Home
②MENU&PRICE
③SALON INFO
④PRODUCTS
⑤COUPON
⑥GALLERY
⑦STAFF
⑧VOICE
⑨RECRUIT
⑩CONTACT
⑪BLOG(一覧)
⑫NEWS(一覧)
⑬CAT
⑭HAIR CARE

◇優先事項
1.ユーザビリティー
2.凝ったデザイン
3.編集更新

◇期待する効果
1.新規顧客の獲得
2.既存顧客の満足度向上
3.イメージアップ

◇ターゲット
【性別】男女比(男1 : 9女)
【年代】30代~40代
【属性】会社員 自営業 主婦

◇sns
Facebook 会社用

◇テイスト
◯シンプル ナチュラル かっこいい
×可愛い・キュート カラフル 高級感

※デザインのテイストとして僕自身の好みですが、ペンキの質感やコンクリートの質感が好きで、シンプルの中にかっこよさがあるデザインが好きです。
(少しでも参考にして頂ければ嬉しいです)

◇希望カラー
ベース色(ベージュ・白)
差し色 (茶系・緑系 アースカラー)
サイトURL
http://mizutama2047.com/
ページ数
1ページ
希望イメージ
シンプル 複雑
単色 カラフル
暗い 明るい
日常 高級
遊び心 厳粛
未来的 伝統的
女性的 男性的
希望する色
茶系、緑系、グレー系、ペースは白系で考えています。そのほかは茶色や緑が好きです。
納品ファイル
• イラストレーター形式 (.ai)
• フォトショップ形式 (.psd)
• PNG形式 (.png)
補足説明
素材①
撮影データをナギボックスドライブにアップしています。
下記URLよりダウンロードしてください。
http://nagibox.jp/download/c51e7a02d9b3f684e10a7c2bd5f93e8a61c04d77
ダウンロードパスワード pass

※素材として、コンクリートの写真があり、店内の打ちっぱなしの部分になりますが、上手く背景などで使えたらと思い写真を取りました、使えなさそうであれば無視して頂いても構いません。

素材➁
クレパド:https://jp.krepado.com/
当院で定期契約をしています。クレジット購入のみのもの以外をご利用下さい。
また定期契約のものは当院の負担となり、ランサー様に負担はありません。
カンプ画像を入れてください。
依頼公開後の追記内容
素材のダウンロードリンクが切れてしまっていたので再度アップロード致します。
ダウンロードをお願い致します。
http://nagibox.jp/download/9e4c1b7a35d0f28e6a17c9b4e02d5f3a8b76c1e9

ダウンロードパスワード pass

作成期間が少なくなってしまった人もいるので延長させていただきます。
もう少し提案が見たいため、延長させて頂きます。
■ 選んだ理由

デザインが良かったので選定致しました。

■ 提案者全員のお礼・コメント

皆様素敵なデザインをありがとうございました。

```html
<!DOCTYPE html>
<html lang="ja">
<head>
<meta charset="utf-8">
<title>MIZUTAMA hair salon</title>
<link href="https://fonts.googleapis.com/css2?family=Noto+Sans+JP:wght@400;500;700&family=Noto+Serif+JP:wght@400;600&family=Cormorant+Garamond:wght@500;600&display=swap" rel="stylesheet">
<style>
:root{
  --bg:#ececea;
  --panel:#ffffff;
  --panel-soft:#f7f7f5;
  --ink:#4a4a48;
  --ink-soft:#8a8a86;
  --line:#d8d8d4;
  --green:#8ab04a;
  --green-dark:#6f9634;
  --green-pale:#c9dc9f;
  --brown:#7a5c3e;
  --pink:#f3b7c8;
  --purple:#c9a3d9;
  --grey-cell:#bdbdb8;
}
*{box-sizing:border-box;margin:0;padding:0}
html,body{width:1200px;height:3000px;overflow:hidden}
body{background:linear-gradient(180deg,#e9e9e6 0%,#efefec 60%,#f4f4f1 100%);font-family:"Noto Sans JP",sans-serif;color:var(--ink);position:relative}
.page{position:relative;width:1200px;height:3000px}

/* sidebar */
.sidebar{position:absolute;left:0;top:0;width:250px;height:800px;background:rgba(255,255,255,.85);padding:40px 0 0}
.brand{display:flex;align-items:center;justify-content:center;gap:10px;font-family:"Noto Serif JP",serif;font-weight:600;font-size:30px;letter-spacing:3px;color:var(--ink);height:120px}
.brand-dot{width:12px;height:12px;border-radius:50%;background:var(--green)}
.nav{list-style:none;margin-top:20px}
.nav li{font-family:"Cormorant Garamond",serif;font-weight:600;font-size:20px;letter-spacing:1px;padding:3px 0 3px 44px;color:var(--ink)}
.nav li.current{background:var(--green-pale);color:var(--ink);position:relative}
.nav li.current::before{content:"";position:absolute;left:24px;top:11px;width:8px;height:8px;border-radius:50%;background:var(--green-dark)}
.reserve{display:block;margin:40px auto 0;width:160px;height:52px;background:var(--green);color:#fff;text-align:center;font-weight:700;font-size:22px;line-height:40px;position:relative}
.reserve small{position:absolute;left:0;right:0;bottom:3px;font-size:9px;line-height:1;font-weight:400;letter-spacing:1px}
.side-tel{margin:14px 0 0 24px;font-size:18px;color:var(--green-dark);font-weight:500}
.side-addr{margin:6px 24px 0;font-size:11px;line-height:1.6;color:var(--ink-soft)}
.social{display:flex;gap:10px;margin:20px 0 0 26px}
.social span{width:26px;height:26px;border-radius:50%;background:var(--green-pale)}

/* hero */
.hero{position:absolute;left:320px;top:152px;width:810px;height:520px;background:linear-gradient(135deg,#3b2f24 0%,#8a6a48 35%,#d9c7a8 55%,#6a5640 80%,#2d241c 100%)}
.dots{position:absolute;left:690px;top:662px;display:flex;gap:8px}
.dots span{width:7px;height:7px;border-radius:50%;background:#ccc}
.dots span.on{background:#888}

.section-title{font-family:"Cormorant Garamond",serif;font-weight:600;font-size:22px;letter-spacing:3px;text-align:center;color:var(--ink)}
.section-title::after{content:"";display:block;width:100%;height:1px;background:var(--line);margin-top:6px}

/* news */
.news{position:absolute;left:330px;top:740px;width:780px;height:340px;background:var(--panel-soft);padding:0 20px}
.news .section-title{padding-top:6px}
.news-item{padding:16px 0;border-bottom:1px solid var(--line);font-size:11px;line-height:1.7;color:var(--ink-soft)}
.news-item time{display:block;font-size:11px;color:var(--ink)}

/* staff & blog */
.staff{position:absolute;left:370px;top:1160px;width:380px;display:grid;grid-template-columns:1fr 1fr;column-gap:40px;row-gap:30px}
.staff-card{text-align:center;font-size:10px}
.staff-card .role{font-family:"Cormorant Garamond",serif;font-size:13px;letter-spacing:2px}
.avatar{width:150px;height:150px;border-radius:50%;margin:4px auto 8px;background:var(--grey-cell);color:#fff;font-family:"Cormorant Garamond",serif;font-size:26px;display:flex;align-items:center;justify-content:center;text-align:center;line-height:1.1}
.avatar.photo{background:linear-gradient(160deg,#5a7aa0,#c8ccd2 60%,#7a6a5a)}
.staff-card .name{font-size:11px;margin-bottom:4px}
.staff-card p{color:var(--ink-soft);line-height:1.6;text-align:left;padding:0 6px}

.blog{position:absolute;left:780px;top:1175px;width:300px}
.blog .section-title{font-size:20px}
.blog-item{padding:12px 0 6px;border-bottom:1px solid var(--line)}
.blog-item h3{font-size:13px;font-weight:500}
.blog-item p{font-size:10px;color:var(--ink-soft);line-height:1.6}
.blog-item time{display:block;text-align:right;font-size:10px;color:var(--ink-soft)}

/* calendar */
.calendar-block{position:absolute;left:330px;top:1840px;width:780px}
.cal-wrap{display:flex;gap:30px;margin-top:20px}
.cal-news{width:260px;font-size:10px;color:var(--ink-soft);line-height:1.6}
.cal-news time{color:var(--ink);display:block}
.cal-news div{margin-bottom:8px}
.cal-reserve{display:block;width:150px;height:46px;margin:10px auto 0;background:var(--green);color:#fff;text-align:center;font-weight:700;font-size:20px;line-height:36px;position:relative}
.cal-reserve small{position:absolute;left:0;right:0;bottom:3px;font-size:8px;line-height:1;font-weight:400}
.cal-tel{text-align:center;color:var(--green-dark);font-size:15px;margin-top:6px}
.cal{flex:1}
.cal-head{background:var(--green);color:#fff;height:46px;display:flex;align-items:center;justify-content:space-between;padding:0 16px;font-family:"Cormorant Garamond",serif;font-size:26px}
.cal-head span{font-size:13px;font-family:"Noto Sans JP",sans-serif}
table{width:100%;border-collapse:separate;border-spacing:3px;margin-top:4px}
td,th{height:36px;text-align:center;font-size:14px;background:#fff;border:1px solid var(--line)}
th{height:22px;font-size:10px;background:var(--green-pale);border:none}
td.empty{background:transparent;border:none}
td.off{background:var(--pink)}
td.event{background:var(--purple)}

/* access */
.access{position:absolute;left:330px;top:2290px;width:780px}
.access-body{display:flex;gap:30px;margin-top:24px}
.access-info{width:240px;font-size:11px;line-height:1.8;color:var(--ink)}
.shop-photo{width:240px;height:110px;background:linear-gradient(135deg,#7a6650,#d7cbb5 60%,#8a7a64);margin-bottom:12px}
.access-info .tel{font-size:16px;margin-top:10px}
.map{flex:1;height:260px;background:linear-gradient(135deg,#f1eee7,#e7e2d6 50%,#f3efe4);border:1px solid var(--line)}

/* footer */
.footer{position:absolute;left:0;bottom:0;width:1200px;height:250px;background:var(--green)}
.grass{position:absolute;left:0;top:-40px;width:1200px;height:60px}
.foot-nav{position:absolute;top:70px;width:100%;text-align:center;color:#fff;font-family:"Cormorant Garamond",serif;font-weight:600;font-size:15px;letter-spacing:1px}
.foot-brand{position:absolute;top:110px;width:100%;text-align:center;color:#fff;font-family:"Noto Serif JP",serif;font-weight:600;font-size:24px;letter-spacing:3px}
.foot-addr{position:absolute;top:150px;width:100%;text-align:center;color:#fff;font-size:10px}
.copy{position:absolute;top:172px;width:100%;text-align:center;color:#eef5e0;font-size:9px}
.totop{position:absolute;right:30px;top:-70px;width:56px;height:56px;border-radius:50%;background:var(--green-pale);color:#fff;font-size:10px;display:flex;align-items:center;justify-content:center}
</style>
</head>
<body>
<div class="page">

<aside class="sidebar">
  <div class="brand"><span class="brand-dot"></span>MIZUTAMA</div>
  <ul class="nav">
    <li class="current">HOME</li>
    <li>MENU&amp;PRICE</li>
    <li>SALON INFO</li>
    <li>PRODUCTS</li>
    <li>COUPON</li>
    <li>GALLERY</li>
    <li>STAFF</li>
    <li>VOICE</li>
    <li>RECRUIT</li>
    <li>CONTACT</li>
  </ul>
  <a class="reserve">ご予約<small>RESERVATION</small></a>
  <p class="side-tel">Tel.075-410-2286</p>
  <p class="side-addr">営業時間 10:00〜19:00<br>定休日 毎週月曜日・第三火曜日</p>
  <div class="social"><span></span><span></span></div>
</aside>

<div class="hero" role="img" aria-label="サロン店内の写真：鏡とスタイリングチェアが並ぶ"></div>
<div class="dots"><span></span><span class="on"></span><span></span></div>

<section class="news">
  <h2 class="section-title">NEWS</h2>
  <div class="news-item"><time>2017.08.01</time>夏季休業のお知らせです。八月十三日から十六日まではお休みをいただきます。ご予約はお早めにお願いいたします。</div>
  <div class="news-item"><time>2017.07.20</time>新しいヘアケア商品の取り扱いを始めました。店頭にてお試しいただけますので、お気軽にスタッフへお声がけください。</div>
  <div class="news-item"><time>2017.07.01</time>七月のクーポンを更新しました。カットとカラーのセットがお得になっております。詳しくはクーポンページをご覧ください。</div>
</section>

<section class="staff">
  <div class="staff-card"><div class="role">OWNER</div><div class="avatar photo" role="img" aria-label="オーナースタイリストの写真"></div><div class="name">NAME / 名前</div><p>お客様一人ひとりに似合うスタイルをご提案します。</p></div>
  <div class="staff-card"><div class="role">STAFF</div><div class="avatar">No<br>Photo</div><div class="name">NAME / 名前</div><p>丁寧なカウンセリングを心がけています。</p></div>
  <div class="staff-card"><div class="role">STAFF</div><div class="avatar">No<br>Photo</div><div class="name">NAME / 名前</div><p>カラーとヘアケアが得意です。</p></div>
  <div class="staff-card"><div class="role">STAFF</div><div class="avatar">No<br>Photo</div><div class="name">NAME / 名前</div><p>気軽に相談できる空間づくりを。</p></div>
</section>

<section class="blog">
  <h2 class="section-title">BLOG</h2>
  <div class="blog-item"><h3>ブログタイトル</h3><p>本文の一部がここに入ります。本文の一部がここに入ります。</p><time>2017.08.01</time></div>
  <div class="blog-item"><h3>ブログタイトル</h3><p>本文の一部がここに入ります。本文の一部がここに入ります。</p><time>2017.07.28</time></div>
  <div class="blog-item"><h3>ブログタイトル</h3><p>本文の一部がここに入ります。本文の一部がここに入ります。</p><time>2017.07.21</time></div>
  <div class="blog-item"><h3>ブログタイトル</h3><p>本文の一部がここに入ります。本文の一部がここに入ります。</p><time>2017.07.14</time></div>
  <div class="blog-item"><h3>ブログタイトル</h3><p>本文の一部がここに入ります。本文の一部がここに入ります。</p><time>2017.07.07</time></div>
</section>

<section class="calendar-block">
  <h2 class="section-title">CALENDAR</h2>
  <div class="cal-wrap">
    <div class="cal-news">
      <div><time>2017.08.06</time>臨時休業となります。</div>
      <div><time>2017.08.13</time>イベント開催日です。</div>
      <div><time>2017.08.27</time>午後のみ営業いたします。</div>
      <a class="cal-reserve">ご予約<small>RESERVATION</small></a>
      <p class="cal-tel">075-410-2286</p>
    </div>
    <div class="cal">
      <div class="cal-head">August<span>2017</span></div>
      <table>
        <tr><th>SUN</th><th>MON</th><th>TUE</th><th>WED</th><th>THU</th><th>FRI</th><th>SAT</th></tr>
        <tr><td class="empty"></td><td class="empty"></td><td>1</td><td>2</td><td>3</td><td>4</td><td>5</td></tr>
        <tr><td class="off">6</td><td class="off">7</td><td>8</td><td>9</td><td>10</td><td>11</td><td>12</td></tr>
        <tr><td class="event">13</td><td>14</td><td>15</td><td>16</td><td>17</td><td>18</td><td>19</td></tr>
        <tr><td>20</td><td>21</td><td>22</td><td>23</td><td>24</td><td>25</td><td>26</td></tr>
        <tr><td class="event">27</td><td>28</td><td>29</td><td>30</td><td>31</td><td class="empty"></td><td class="empty"></td></tr>
      </table>
    </div>
  </div>
</section>

<section class="access">
  <h2 class="section-title">ACCESS</h2>
  <div class="access-body">
    <div class="access-info">
      <div class="shop-photo" role="img" aria-label="サロン外観の写真"></div>
      〒000-0000<br>京都府水玉市中央町 1-2-3<br>・最寄駅から徒歩5分<br>・駐車場2台あり
      <p class="tel">Tel. 075-410-2286</p>
    </div>
    <div class="map" role="img" aria-label="サロン周辺の地図"></div>
  </div>
</section>

<footer class="footer">
  <svg class="grass" viewBox="0 0 1200 60" preserveAspectRatio="none"><path d="M0 60 L0 30 Q30 10 60 30 Q90 5 120 28 Q160 12 200 32 Q240 8 280 30 Q320 14 360 28 Q400 6 440 30 Q480 16 520 26 Q560 4 600 30 Q640 14 680 28 Q720 8 760 32 Q800 12 840 28 Q880 6 920 30 Q960 14 1000 28 Q1040 8 1080 30 Q1120 12 1160 28 Q1180 20 1200 30 L1200 60 Z" fill="#8ab04a"/></svg>
  <div class="totop">TOP</div>
  <nav class="foot-nav">HOME ｜ MENU&amp;PRICE ｜ SALON INFO ｜ PRODUCTS ｜ COUPON ｜ GALLERY ｜ STAFF ｜ VOICE ｜ RECRUIT ｜ CONTACT</nav>
  <div class="foot-brand">MIZUTAMA</div>
  <p class="foot-addr">〒000-0000 京都府水玉市中央町 1-2-3 Tel.075-410-2286</p>
  <p class="copy">copyright © MIZUTAMA All rights reserved.</p>
</footer>

</div>
</body>
</html>
```